Creating a Label for the Wine "Marvessa"

Marvessa
As you know Marvessa is an imagined place or state of things in which everything is perfect. This wine reflects that. It is a high value wine and it is perfect. The dimensions shoulb be between 9c x 11,5 cm and 12cm x 8 cm

```html
<!DOCTYPE html>
<html lang="en">
<head>
<meta charset="utf-8">
<title>Marvessa Wine Label</title>
<link rel="stylesheet" href="https://fonts.googleapis.com/css2?family=Poiret+One&family=Montserrat:wght@300;600&display=swap">
<style>
  :root {
    --paper: #ffffff;
    --navy-deep: #0a0634;
    --navy-mid: #1a1660;
    --navy-light: #2e3190;
    --silver: #9a9a9a;
    --silver-light: #d8d8d8;
    --label-white: #ffffff;
    --label-grey: #b9b9c4;
  }
  html, body {
    margin: 0;
    padding: 0;
    width: 1200px;
    height: 903px;
    overflow: hidden;
    background: var(--paper);
  }
  .canvas {
    position: relative;
    width: 1200px;
    height: 903px;
    background: var(--paper);
  }
  .label {
    position: absolute;
    left: 0;
    top: 0;
  }
  .wine-name {
    font-family: "Poiret One", sans-serif;
    font-size: 84px;
    fill: var(--label-white);
    letter-spacing: 4px;
  }
  .estate-line {
    font-family: "Montserrat", sans-serif;
    font-size: 17px;
    letter-spacing: 5px;
  }
  .estate-name {
    font-weight: 600;
    fill: var(--label-white);
  }
  .estate-word {
    font-weight: 300;
    fill: var(--label-grey);
  }
</style>
</head>
<body>
<main class="canvas">
  <svg class="label" width="1200" height="903" viewBox="0 0 1200 903" aria-label="Marvessa Vineyards round wine label">
    <defs>
      <linearGradient id="label-field" x1="1" y1="0" x2="0" y2="1">
        <stop offset="0" stop-color="var(--navy-light)"/>
        <stop offset="0.55" stop-color="var(--navy-deep)"/>
        <stop offset="1" stop-color="var(--navy-mid)"/>
      </linearGradient>
      <linearGradient id="label-rim" x1="0" y1="1" x2="1" y2="0">
        <stop offset="0" stop-color="var(--navy-light)"/>
        <stop offset="0.5" stop-color="var(--navy-deep)"/>
        <stop offset="1" stop-color="var(--navy-deep)"/>
      </linearGradient>
      <linearGradient id="silver-edge" x1="0" y1="0" x2="1" y2="1">
        <stop offset="0" stop-color="var(--silver)"/>
        <stop offset="0.5" stop-color="var(--silver-light)"/>
        <stop offset="1" stop-color="var(--silver)"/>
      </linearGradient>
      <path id="estate-arc" d="M 430 560 A 210 210 0 0 0 780 560"/>
    </defs>

    <!-- silver outer edge -->
    <circle class="silver-ring" cx="605" cy="448" r="255" fill="none" stroke="url(#silver-edge)" stroke-width="4"/>
    <!-- navy rim -->
    <circle class="navy-rim" cx="605" cy="448" r="247" fill="url(#label-rim)"/>
    <!-- navy field -->
    <circle class="navy-field" cx="605" cy="448" r="236" fill="url(#label-field)"/>

    <text class="wine-name" x="605" y="0" text-anchor="middle" transform="translate(0 521) scale(1 2)">MARVESSA</text>

    <text class="estate-line">
      <textPath href="#estate-arc" startOffset="50%" text-anchor="middle"><tspan class="estate-name">MARVESSA</tspan><tspan class="estate-word"> VINEYARDS</tspan></textPath>
    </text>
  </svg>
</main>
</body>
</html>
```